Postcard Design for a cafe in Redfern NSW Australia

I need a postcard design to help promote my cafe located in Redfern NSW Australia. The aim of the postcard is to let people in the local area know about the cafe and to entice them to try us out. Another aim is to try to increase our take away coffee sales during the week. All our food is freshly made and we also sell freshly made juices and smoothies. The name of the cafe is Tin Kettle Cafe. Our goal is to offer good food and coffee in a friendly and relaxed environment. We hope that people come to the cafe and leave feeling relaxed and full! We use our own coffee blend called "Quiet Tide Blend" . The address is 42 Malvina Street, Redfern website is www.tinkettlecafe.com.au. I also would like the QR Code provided on the Post card.

Target Market(s)

People that live in the local area (Redfern and surrounding suburbs), aged between 25 and 65

Industry/Entity Type

Cafe

Font styles to use
Serif

Colors
fbed22

Requirements
Must have
• The Coffee Logo(file 2) "Quiet Tide Blend" should be in one side of the postcard by itself.
Nice to have
• A classy postcard
Should not have
• Cheesy pictures of food

```html
<!DOCTYPE html>
<html lang="en">
<head>
<meta charset="utf-8">
<title>Tin Kettle Cafe – Postcard</title>
<link rel="stylesheet" href="https://fonts.googleapis.com/css2?family=Libre+Baskerville&family=PT+Sans:wght@700&family=PT+Sans+Narrow:wght@400;700&display=swap">
<style>
  :root {
    --backdrop: #4d4d4d;
    --card: #ffffff;
    --card-shade: #f3f3f3;
    --brand-yellow: #fbed22;
    --logo-yellow: #f5ea1c;
    --ink: #231a12;
    --coffee-dark: #2e1a0e;
    --coffee-mid: #5a3620;
    --burlap: #9c8467;
    --on-photo: #ffffff;
    --stamp-frame: #ececec;
    --stamp-fill: #e3e3e3;
    --stamp-text: #fafafa;
    --write-line: #e4e4e4;
  }
  * { margin: 0; padding: 0; box-sizing: border-box; }
  html, body { width: 1200px; height: 903px; overflow: hidden; }
  body { background: var(--backdrop); position: relative; }

  .postcard {
    position: absolute; left: 121px; top: 88px;
    width: 958px; height: 730px;
    background: linear-gradient(135deg, var(--card) 40%, var(--card-shade));
  }

  /* Message side */
  .promo { position: absolute; left: 0; top: 0; width: 460px; height: 617px; }
  .promo__header {
    position: absolute; left: 0; top: 0; width: 460px; height: 299px;
    background: var(--brand-yellow);
  }
  .brand {
    position: absolute; left: 80px; top: 17px; width: 288px; height: 165px;
    background: var(--logo-yellow);
  }
  .brand__name {
    position: absolute; left: 0; top: 100px; width: 288px; text-align: center;
    font-family: "PT Sans Narrow", sans-serif; font-weight: 700;
    font-size: 43px; line-height: 50px; letter-spacing: 2.5px;
    color: var(--ink); white-space: nowrap;
  }
  .brand__blend {
    position: absolute; left: 0; top: 143px; width: 288px; text-align: center;
    font-family: "PT Sans Narrow", sans-serif; font-weight: 700;
    font-size: 14px; line-height: 16px; letter-spacing: 6px;
    color: var(--ink); white-space: nowrap;
  }
  .brand__rule {
    position: absolute; left: 90px; top: 188px; width: 268px; height: 1px;
    background: var(--ink);
  }
  .orders {
    position: absolute; left: 0; top: 230px; width: 460px; text-align: center;
    color: var(--ink);
  }
  .orders__label {
    font-family: "PT Sans Narrow", sans-serif;
    font-size: 19px; letter-spacing: 0.6px; line-height: 22px;
  }
  .orders__phone {
    font-family: "PT Sans", sans-serif; font-weight: 700;
    font-size: 28px; line-height: 36px; letter-spacing: 0.3px;
  }

  .promo__photo {
    position: absolute; left: 0; top: 299px; width: 460px; height: 318px;
    border-bottom-right-radius: 42px; overflow: hidden;
    background:
      radial-gradient(ellipse 60% 40% at 30% 18%, var(--burlap), transparent 70%),
      linear-gradient(160deg, var(--coffee-mid), var(--coffee-dark) 75%);
  }
  .details {
    position: absolute; left: 0; top: 470px; width: 460px; text-align: center;
    font-family: "Libre Baskerville", serif; color: var(--on-photo);
  }
  .details__hours { font-size: 16px; line-height: 24px; }
  .details__rule { width: 240px; height: 1px; background: var(--on-photo); margin: 12px 0 8px 117px; }
  .details__address, .details__web { font-size: 18px; line-height: 33px; letter-spacing: 0.4px; white-space: nowrap; }

  /* Address side */
  .stamp {
    position: absolute; left: 748px; top: 19px; width: 177px; height: 179px;
    background: var(--stamp-frame); padding: 10px;
  }
  .stamp__box {
    width: 100%; height: 100%; background: var(--stamp-fill);
    display: flex; align-items: center; justify-content: center; text-align: center;
    font-family: "PT Sans Narrow", sans-serif; font-size: 27px; line-height: 38px;
    letter-spacing: 1px; color: var(--stamp-text);
  }
  .address-lines { position: absolute; left: 498px; top: 297px; width: 427px; }
  .address-lines li {
    list-style: none; height: 2px; background: var(--write-line); margin-bottom: 48px;
  }
</style>
</head>
<body>
  <article class="postcard">
    <section class="promo">
      <header class="promo__header">
        <div class="brand">
          <p class="brand__name">Tin Kettle Cafe</p>
          <p class="brand__blend">QUIET TIDE BLEND</p>
        </div>
        <div class="brand__rule"></div>
        <div class="orders">
          <p class="orders__label">TAKE AWAY PHONE ORDERS</p>
          <p class="orders__phone">(02)95550147</p>
        </div>
      </header>
      <div class="promo__photo" role="img" aria-label="Roasted coffee beans spilling from a burlap sack with a wooden scoop"></div>
      <div class="details">
        <p class="details__hours">Breakfast and lunch:<br>daily from 8 am to 4 pm</p>
        <div class="details__rule"></div>
        <p class="details__address">42 Malvina Street, Redfern</p>
        <p class="details__web">www.tinkettlecafe.com.au.</p>
      </div>
    </section>

    <div class="stamp"><div class="stamp__box">PLACE<br>STAMP<br>HERE</div></div>
    <ul class="address-lines">
      <li></li><li></li><li></li><li></li><li></li><li></li>
    </ul>
  </article>
</body>
</html>
```